Heating and Cooling Company mobile website

We need a website specifically designed for a viewing on a mobile device.

We serve the northern New Jersey heating, cooling and electrical residential market.

The goal is the drive traffic to the site by using Brindle Pay Per click. People will be searching for an HVAC contractor, and they land on our page. They need to get key info quickly without all the clutter of a desktop type of site.

Target Market(s)

Homeowners

Industry/Entity Type

Hvac

Coding

Coded - Design and coding required

Number of Pages Required

5+ page

Font styles to use
Serif

Requirements
Must have
• View attachments to see samples of the desktop version. It must have a similar color scheme
• The copy of the website is also attached
Nice to have
• Would like it to have a sort of Quello feel to it. Make it seem like its an app that people are using and that its exciting to be on the website. It would be nice to have a page where customers can book appointments

```html
<!DOCTYPE html>
<html lang="en">
<head>
<meta charset="utf-8">
<title>Warmhaven Heating &amp; Cooling</title>
<link rel="stylesheet" href="https://fonts.googleapis.com/css2?family=Montserrat:ital,wght@0,400;0,500;0,600;0,700;0,800;1,400&display=swap">
<style>
  :root {
    --navy: #34406a;
    --navy-deep: #2e3a60;
    --red: #9b1c26;
    --cream: #f3ead6;
    --beige: #ebe3d3;
    --hero-light: #ddd5c7;
    --hero-dark: #bfb6a7;
    --grey: #8d8f96;
    --white: #ffffff;
  }
  * { box-sizing: border-box; margin: 0; padding: 0; }
  html, body {
    width: 845px; height: 1200px; overflow: hidden;
    background: var(--white);
    font-family: "Montserrat", Arial, sans-serif;
    color: var(--navy);
  }
  .site { width: 845px; height: 1200px; display: flex; flex-direction: column; }

  .site-header {
    height: 130px; background: var(--navy);
    display: flex; align-items: center; justify-content: space-between;
    padding: 0 36px 0 40px;
  }
  .menu-toggle { width: 40px; display: flex; flex-direction: column; gap: 11px; }
  .menu-toggle span { display: block; height: 3px; background: var(--white); border-radius: 2px; }
  .brand-name {
    font-weight: 700; font-size: 40px; letter-spacing: 1px;
    color: var(--cream);
  }
  .social { display: flex; gap: 16px; }
  .social span {
    width: 40px; height: 40px; border-radius: 50%;
    border: 2.5px solid var(--white);
  }

  .hero {
    position: relative; height: 480px;
    background: linear-gradient(135deg, var(--hero-light) 0%, #d3cabc 55%, var(--hero-dark) 100%);
    padding: 150px 0 0 90px;
  }
  .hero-eyebrow {
    font-size: 25px; font-weight: 700; letter-spacing: 10px;
    color: var(--red); margin-bottom: 18px;
  }
  .hero-title {
    font-size: 44px; font-weight: 800; line-height: 1.2; color: var(--navy);
  }
  .hero-title .sub { font-weight: 600; display: block; }
  .hero-title em { font-style: normal; color: var(--red); font-weight: 800; }

  .pill-button {
    display: inline-flex; align-items: center; justify-content: center; gap: 18px;
    height: 86px; padding: 0 52px;
    border: 2.5px solid var(--navy); border-radius: 43px;
    font-size: 23px; font-weight: 600; letter-spacing: 6px;
    color: var(--navy); text-decoration: none;
  }
  .hero .pill-button { margin-top: 44px; width: 324px; padding: 0; }

  .services { height: 260px; background: var(--white); padding-top: 50px; }
  .section-label {
    text-align: center; font-size: 17px; font-weight: 600;
    letter-spacing: 6px; color: var(--grey);
  }
  .service-list { display: flex; justify-content: space-around; padding: 36px 30px 0; list-style: none; }
  .service { width: 170px; text-align: center; font-size: 20px; font-weight: 500; color: var(--navy); line-height: 1.25; }
  .service svg { display: block; margin: 0 auto 18px; width: 80px; height: 70px; }

  .call-band {
    flex: 1; background: var(--beige);
    text-align: center; padding-top: 62px;
  }
  .call-text {
    font-style: italic; font-size: 29px; line-height: 1.42;
    color: var(--navy); width: 620px; margin: 0 auto 50px;
  }
  .call-band .pill-button { width: 324px; padding: 0; }
</style>
</head>
<body>
<div class="site">
  <header class="site-header">
    <div class="menu-toggle" aria-label="Menu"><span></span><span></span><span></span></div>
    <div class="brand-name">Warmhaven</div>
    <div class="social" aria-label="Social links"><span></span><span></span></div>
  </header>

  <section class="hero" role="img" aria-label="City street with a company service van, softly washed in beige">
    <p class="hero-eyebrow">THE BEST WAY</p>
    <h1 class="hero-title">TO LIVE IN NEW JERSEY<span class="sub">Is With <em>Comfort!</em></span></h1>
    <a class="pill-button" href="#">LEARN MORE</a>
  </section>

  <section class="services">
    <p class="section-label">OUR SERVICES</p>
    <ul class="service-list">
      <li class="service">
        <svg viewBox="0 0 80 70" fill="none" stroke="#34406a" stroke-width="3" stroke-linecap="round">
          <path d="M20 38a20 20 0 0 1 40 0Z" fill="#9b1c26" stroke="none"/>
          <path d="M40 4v8M18 12l5 6M62 12l-5 6M8 28h8M64 28h8"/>
          <path d="M6 44h68M10 52q7-4 15 0t15 0 15 0 15 0M16 60q6-3 12 0t12 0 12 0 12 0"/>
        </svg>
        Heating
      </li>
      <li class="service">
        <svg viewBox="0 0 80 70" fill="none" stroke="#34406a" stroke-width="3" stroke-linecap="round">
          <rect x="6" y="10" width="68" height="26" rx="3" fill="#9b1c26" stroke="#34406a"/>
          <path d="M14 20h52M14 27h52" stroke="#fff" stroke-width="2"/>
          <path d="M26 46l-4 10M40 46v10M54 46l4 10"/>
        </svg>
        Air<br>conditioning
      </li>
      <li class="service">
        <svg viewBox="0 0 80 70" fill="none" stroke="#34406a" stroke-width="3" stroke-linecap="round">
          <path d="M40 4q-10 0-10 8t10 8"/>
          <path d="M34 22h12v8H34Z" fill="#34406a"/>
          <path d="M28 30h24v14q0 8-12 8t-12-8Z" fill="#9b1c26"/>
          <path d="M34 52v12M46 52v12"/>
        </svg>
        Electrical
      </li>
      <li class="service">
        <svg viewBox="0 0 80 70" fill="none" stroke="#34406a" stroke-width="3" stroke-linejoin="round">
          <circle cx="40" cy="35" r="5" fill="#9b1c26"/>
          <path d="M40 30q-4-20 10-24t4 18Z"/>
          <path d="M45 35q20-4 24 10t-18 4Z"/>
          <path d="M40 40q4 20-10 24t-4-18Z"/>
          <path d="M35 35q-20 4-24-10t18-4Z"/>
        </svg>
        Ventilation
      </li>
    </ul>
  </section>

  <section class="call-band">
    <p class="call-text">Seriously, don't be afraid to call at any time, we live for this, just give us a min to get&nbsp; some coffee on the way over.</p>
    <a class="pill-button" href="#">
      <svg width="20" height="34" viewBox="0 0 20 34" fill="none" stroke="#34406a" stroke-width="2.5">
        <rect x="2" y="2" width="16" height="30" rx="3"/>
        <path d="M8 27h4"/>
      </svg>
      CALL NOW
    </a>
  </section>
</div>
</body>
</html>
```